Thai Takeaway Menu Design

I need a menu re-design for a thai takeaway/restaurant in australia.

Please use content from the existing menu
http://www.platterwink.example/u/menu/7302918?p=1

I'd like to emphasise on
1 - free delivery for order over $40
2 - gluten free and vegetatian option available on most meal (however you want to word it - not fuss)

*remove (the banner order online and save $10)

I'm happy to change the whole concept & design. I particularly like rustic, raw look more than moden ones. Does not need to be flowery or anything like current one :)

Industry/Entity Type

Restaurant

```html
<!DOCTYPE html>
<html lang="en">
<head>
<meta charset="utf-8">
<title>Thai Takeaway Menu</title>
<link href="https://fonts.googleapis.com/css2?family=Tinos:wght@400;700&display=swap" rel="stylesheet">
<style>
:root{
  --wood-dark:#4a3417;
  --wood-mid:#7a5a2c;
  --wood-light:#9a7a45;
  --panel-core:#f2d36a;
  --panel-edge:#d9b247;
  --ink:#1c1206;
  --note:#f6efd8;
  --trim:#2a1c0a;
}
*{margin:0;padding:0;box-sizing:border-box}
html,body{width:1200px;height:854px;overflow:hidden}
body{font-family:"Tinos","Times New Roman",serif;color:var(--ink)}
.menu{
  position:relative;width:1200px;height:854px;overflow:hidden;
  background:
    repeating-linear-gradient(90deg,rgba(40,25,8,.18) 0 3px,transparent 3px 11px,rgba(255,230,170,.05) 11px 14px,transparent 14px 27px),
    linear-gradient(90deg,var(--wood-mid) 0%,var(--wood-dark) 8%,var(--wood-light) 18%,var(--wood-mid) 30%,var(--wood-dark) 40%,var(--wood-light) 52%,var(--wood-mid) 64%,var(--wood-dark) 72%,var(--wood-light) 84%,var(--wood-mid) 94%,var(--wood-dark) 100%);
}
.edge-trim{position:absolute;top:0;bottom:0;width:18px;background:linear-gradient(90deg,var(--trim),#5b4220,var(--trim))}
.edge-trim.left{left:0}
.edge-trim.right{right:0}
.panel{
  position:absolute;top:78px;width:264px;height:668px;
  background:radial-gradient(ellipse at 50% 45%,var(--panel-core) 55%,var(--panel-edge) 100%);
  box-shadow:0 0 16px 8px rgba(242,211,106,.55);
  border-radius:6px;
}
.panel.p1{left:66px}.panel.p2{left:474px}.panel.p3{left:868px}
.section{position:absolute;left:6px;right:10px}
.section h2{font-weight:700;font-size:21px;line-height:26px;text-align:center;margin-bottom:17px}
.section.tight h2{margin-bottom:1px}
.row{display:grid;grid-template-columns:1fr auto;align-items:start;font-size:13.5px;line-height:18.7px;column-gap:6px}
.row.price-low{align-items:end}
.row .price{text-align:right;min-width:48px}
.note{position:absolute;top:776px;font-size:15px;font-weight:700;color:var(--note);white-space:nowrap}
.note.veg{left:857px}
.note.delivery{left:66px}
.note.gluten{left:474px}
</style>
</head>
<body>
<main class="menu">
  <div class="edge-trim left" role="img" aria-label="Carved ornamental border"></div>
  <div class="edge-trim right" role="img" aria-label="Carved ornamental border"></div>

  <section class="panel p1">
    <div class="section" style="top:7px">
      <h2>Entrée</h2>
      <div class="row"><span>Spring Rolls *(4)</span><span class="price">$6.00</span></div>
      <div class="row"><span>Satay Chicken (4)</span><span class="price">$6.00</span></div>
      <div class="row"><span>Fish Cakes &nbsp;(4)</span><span class="price">$6.00</span></div>
      <div class="row"><span>Dim Sim (4)</span><span class="price">$6.00</span></div>
      <div class="row"><span>Duck Rice Paper Rolls*(2)</span><span class="price">$6.00</span></div>
      <div class="row"><span>Papaya Salad</span><span class="price">$6.00</span></div>
      <div class="row"><span>Tofu &nbsp;W/ Peanut Sauce *</span><span class="price">$6.00</span></div>
    </div>
    <div class="section" style="top:187px">
      <h2>Soup</h2>
      <div class="row"><span>Tom Yum Prawn*</span><span class="price">$7.00</span></div>
      <div class="row"><span>Tom Kha Chicken*</span><span class="price">$7.00</span></div>
    </div>
    <div class="section" style="top:274px">
      <h2>Curry</h2>
      <div class="row"><span>Green Curry Chicken*</span><span class="price">$12.90</span></div>
      <div class="row"><span>Panang Chicken*</span><span class="price">$12.90</span></div>
      <div class="row"><span>Red Curry Beef*</span><span class="price">$12.90</span></div>
      <div class="row"><span>Massaman Beef Curry</span><span class="price">$12.90</span></div>
      <div class="row"><span>Red Duck Curry</span><span class="price">$16.90</span></div>
      <div class="row"><span>Yellow Curry Chicken*</span><span class="price">$12.90</span></div>
      <div class="row"><span>Yellow Curry Prawn</span><span class="price">$16.90</span></div>
    </div>
    <div class="section" style="top:454px">
      <h2>Vegetable</h2>
      <div class="row"><span>Mixed Vegetables*</span><span class="price">$10.50</span></div>
      <div class="row"><span>Steamed Veg W/ Peanut Sauce*</span><span class="price">$10.50</span></div>
    </div>
    <div class="section" style="top:540px">
      <h2>Beef</h2>
      <div class="row"><span>Beef W/ Oyster Sauce*</span><span class="price">$12.90</span></div>
      <div class="row"><span>Grilled Beef Salad*</span><span class="price">$12.90</span></div>
    </div>
  </section>

  <section class="panel p2">
    <div class="section" style="top:7px">
      <h2>Chicken</h2>
      <div class="row"><span>Laab Chicken*</span><span class="price">$12.90</span></div>
      <div class="row"><span>Chicken W/ Sweet Basil*</span><span class="price">$12.90</span></div>
      <div class="row"><span>Chicken W/ Cashew Nuts*</span><span class="price">$12.90</span></div>
      <div class="row"><span>Grilled Chicken W/ Salad</span><span class="price">$12.90</span></div>
      <div class="row"><span>Southern Style Fried Chicken</span><span class="price">$12.90</span></div>
    </div>
    <div class="section" style="top:150px">
      <h2>Pork</h2>
      <div class="row"><span>Sweet &amp; Sour Pork*</span><span class="price">$12.90</span></div>
      <div class="row"><span>Garlic Pork</span><span class="price">$12.90</span></div>
      <div class="row"><span>Cripy Pork W/ Asian Greens*</span><span class="price">$12.90</span></div>
    </div>
    <div class="section" style="top:255px">
      <h2>Duck</h2>
      <div class="row"><span>Roast Duck W/<br>Vegetable &amp; Gravy</span><span class="price">$12.90</span></div>
      <div class="row"><span>Duck W/ Sweet Basil</span><span class="price">$12.90</span></div>
      <div class="row price-low"><span>Honey Glazed Duck<br>W/ Vegetable</span><span class="price">$12.90</span></div>
    </div>
    <div class="section" style="top:398px">
      <h2>Seafood</h2>
      <div class="row"><span>Garlic Prawn</span><span class="price">$16.90</span></div>
      <div class="row"><span>Tamarind Prawn</span><span class="price">$16.90</span></div>
      <div class="row"><span>Laab Fish</span><span class="price">$16.90</span></div>
      <div class="row"><span>Crispy Fish W/<br>Sweet Chili Salsa</span><span class="price">$16.90</span></div>
      <div class="row"><span>Chili &amp; Lime Calamari Salad</span><span class="price">$16.90</span></div>
      <div class="row"><span>Salt &amp; Pepper Calamari</span><span class="price">$16.90</span></div>
      <div class="row"><span>Spicy Seafood</span><span class="price">$16.90</span></div>
      <div class="row price-low"><span>Crispy Barramundi W/ Green<br>Mango Salad (Seasonal)</span><span class="price">$22.90</span></div>
      <div class="row"><span>Soft Shell Chili Crab</span><span class="price">$22.90</span></div>
    </div>
  </section>

  <section class="panel p3">
    <div class="section" style="top:7px">
      <h2>Noodle</h2>
      <div class="row"><span>Pad Thai*</span><span class="price">$12.50</span></div>
      <div class="row"><span>Pad Thai Prawn</span><span class="price">$16.90</span></div>
      <div class="row"><span>Drunken Noodle*</span><span class="price">$12.50</span></div>
      <div class="row"><span>Pad See Eew*</span><span class="price">$12.50</span></div>
      <div class="row"><span>Beef Noodle Soup</span><span class="price">$12.50</span></div>
      <div class="row"><span>Seafood Laksa</span><span class="price">$16.90</span></div>
    </div>
    <div class="section tight" style="top:169px">
      <h2>Rice</h2>
      <div class="row"><span>Rice (S)</span><span class="price">$2.50</span></div>
      <div class="row"><span>Rice (L)</span><span class="price">$3.50</span></div>
      <div class="row"><span>Coconut Rice (S)</span><span class="price">$4.50</span></div>
      <div class="row"><span>Coconut Rice (L)</span><span class="price">$5.50</span></div>
      <div class="row"><span>Fried Rice</span><span class="price">$10.50</span></div>
      <div class="row"><span>Roti Bread</span><span class="price">$3.50</span></div>
    </div>
    <div class="section" style="top:312px">
      <h2>Dessert</h2>
      <div class="row"><span>Black Sticky Rice<br>W/ Coconut Cream</span><span class="price">$4.50</span></div>
      <div class="row"><span>Tapioca Pudding W/ Lychee</span><span class="price">$4.50</span></div>
    </div>
    <div class="section" style="top:436px">
      <h2>Drinks</h2>
      <div class="row"><span>Kola, Diet Kola, Fizzo, Lumo</span><span class="price"></span></div>
      <div class="row"><span>Zesti- 375 ml</span><span class="price">$2.00</span></div>
      <div class="row"><span>Kola, Fizzo, Lumo - 1.25 L</span><span class="price">$4.50</span></div>
      <div class="row"><span>Orange Juice, Apple Juice</span><span class="price">$3.50</span></div>
      <div class="row"><span>Ginger Beer</span><span class="price">$3.50</span></div>
    </div>
  </section>

  <p class="note delivery">Free Delivery On Orders Over $40</p>
  <p class="note gluten">Gluten Free Options On Most Meals</p>
  <p class="note veg">* Available As Vegetarian Upon Request</p>
</main>
</body>
</html>
```